Solar Flyer-Design
Zielgruppe
Quornel Energie
Für die Firma QuorNel Energie wird ein Flyer im Wickel oder Zickzackfalz Design benötigt. Größe soll Din Lang sein mit insgesamt 6 Seiten.
Es sollen die Inhalte der Webseite (quornel-energie.de bestmöglich verwendet werden.
Aufgabenstellung
Design anhand der Webseite, Bilder auch von der Webseite.
Logo befindet sich im Anhang und Bilder können frei von der Webseite genommen werden, wir besitzen alle Lizenzen daran.

```html
<!DOCTYPE html>
<html lang="de">
<head>
<meta charset="utf-8">
<title>Quornel Energie – Flyer</title>
<link href="https://fonts.googleapis.com/css2?family=Hind:wght@400;500;600&family=Source+Sans+3:wght@600;700;900&display=swap" rel="stylesheet">
<style>
:root{
  --green:#b0cc09;
  --green-text:#a8c70c;
  --ink:#1f1f1f;
  --body:#4a4a4a;
  --white:#ffffff;
  --fold:#cfcfcf;
  --sky:#c9dff0;
  --roof:#2c3e63;
}
*{margin:0;padding:0;box-sizing:border-box}
html,body{width:788px;height:1200px;overflow:hidden;background:var(--white)}
.flyer{position:relative;width:788px;height:1200px;font-family:"Hind",sans-serif;color:var(--body)}
.abs{position:absolute}
.heading{font-family:"Source Sans 3",sans-serif;font-weight:600;color:var(--ink);line-height:1.2}
.copy{font-size:9.6px;line-height:12.9px;text-align:justify}
.fill{border-radius:2px}

/* top row */
.panel-green{left:260px;top:0;width:264px;height:596px;background:var(--green)}
.fold-band{left:0;top:596px;width:788px;height:7px;background:var(--fold)}

.intro-title{left:17px;top:38px;width:240px;font-size:14.2px}
.intro-copy{left:18px;top:102px;width:221px}
.intro-copy p+p{margin-top:13px}
.intro-art{left:10px;top:420px;width:238px;height:160px;border-radius:80px 80px 4px 4px;
  background:linear-gradient(180deg,#dbe9f4 0%,#e7efc9 55%,#f3f3f3 100%)}

.brand-white{left:260px;top:388px;width:264px;text-align:center;color:var(--white);
  font-family:"Source Sans 3",sans-serif;font-weight:700;font-size:17px;letter-spacing:1.5px}
.brand-white .dot{display:inline-block;width:9px;height:9px;border-radius:50%;background:var(--white);margin-right:6px;vertical-align:1px}
.contact{left:260px;top:462px;width:264px;color:var(--white);font-size:8.6px;line-height:10.5px;text-align:center;letter-spacing:.2px}
.contact li{list-style:none;margin-bottom:5px;display:flex;justify-content:center;align-items:flex-start;gap:4px}
.contact svg{flex:none;margin-top:1px}
.partners-label{left:260px;top:543px;width:264px;text-align:center;color:var(--white);font-size:9px;font-weight:500}
.partners{left:278px;top:558px;width:230px;display:flex;justify-content:space-between;align-items:center;
  font-family:"Source Sans 3",sans-serif;font-weight:700;font-size:15px;color:#1d3d8a}

.brand-main{left:555px;top:62px;width:200px;text-align:center;font-family:"Source Sans 3",sans-serif;
  font-weight:900;font-size:25px;color:var(--ink);letter-spacing:1px;line-height:1}
.brand-main .sub{display:block;font-size:25px}
.brand-main .sq{display:inline-block;width:14px;height:14px;background:var(--green);margin-right:8px;vertical-align:1px}
.hero-photo{left:523px;top:157px;width:265px;height:309px;
  background:linear-gradient(180deg,#a9c6e2 0%,#6f8fb9 30%,#2d3d5c 60%,#23314d 100%)}
.hero-title{left:540px;top:490px;width:240px;font-family:"Source Sans 3",sans-serif;font-weight:900;
  font-size:17.2px;line-height:18.2px;color:var(--green-text);letter-spacing:.3px}
.hero-sub{left:540px;top:547px;width:240px;font-size:11.2px;line-height:13.5px;color:var(--body)}

/* bottom row */
.self-title{left:26px;top:632px;width:230px;font-size:13.2px}
.self-copy{left:26px;top:677px;width:225px;text-align:left}
.reasons-title{left:26px;top:720px;font-size:13.2px}
.reasons{left:20px;top:745px;width:232px;list-style:none}
.reasons li{display:flex;gap:7px;font-size:9.6px;line-height:11.7px;margin-bottom:11.3px;min-height:23.4px}
.reasons li svg{flex:none;margin-top:3px}
.reasons-art{left:10px;top:1056px;width:245px;height:140px;border-radius:4px;
  background:linear-gradient(180deg,#e3eef7 0%,#eef4de 55%,#cfe3a4 100%)}

.city-art{left:280px;top:636px;width:225px;height:138px;border-radius:4px;
  background:linear-gradient(180deg,#eef4f9 0%,#f6f2e6 55%,#e0ecd0 100%)}
.mid-copy{left:277px;top:812px;width:214px}
.mid-copy p+p{margin-top:12.9px}

.bg-curve{left:250px;top:940px;width:538px;height:260px}
.install-title{left:543px;top:632px;width:240px;font-size:13.2px}
.install-copy{left:543px;top:671px;width:209px}
.areas{left:544px;top:826px;width:230px;list-style:none}
.areas li{display:flex;align-items:center;font-family:"Source Sans 3",sans-serif;font-weight:700;font-size:17px;color:var(--ink)}
.areas .ico{width:32px;height:32px;border-radius:4px;background:linear-gradient(180deg,#f2b544,#6aa8d8);margin-right:14px;flex:none}
.install-art{left:560px;top:1030px;width:195px;height:140px;border-radius:6px;
  background:linear-gradient(160deg,#ffd66b 0%,#dfe6ec 45%,#b9d67a 100%)}
</style>
</head>
<body>
<main class="flyer">

  <!-- outer side -->
  <div class="abs panel-green"></div>
  <div class="abs fold-band"></div>

  <h2 class="abs heading intro-title">Möchtest Du Deinen eigenen Strom erzeugen und unabhängiger werden?</h2>
  <div class="abs copy intro-copy">
    <p>Dann ist die Photovoltaikanlage eine saubere und umweltfreundliche Lösung.</p>
    <p>Bei uns als Full-Service-Anbieter für PV-Anlagen, für private und gewerbliche Kunden, bist Du an der richtigen Adresse. Gemeinsam mit uns kannst Du Deine PV Anlage planen, abhängig von den örtlichen Gegebenheiten und Deinem Stromverbrauch. Den erzeugten Strom kannst Du selbst nutzen, um Stromkosten zu sparen und/oder ihn an den Örtlichen Stromnetzbe­treiber verkaufen. Mit einer vollumfänglichen PV-Anlage (z.B. mit einem Speicher) senkst Du deine Energiekosten.</p>
  </div>
  <div class="abs fill intro-art" role="img" aria-label="Illustration: Haus mit Solarmodulen auf dem Dach, Sonne, Bäume und ein Mann davor"></div>

  <div class="abs brand-white"><span class="dot"></span>QUORNEL ENERGIE</div>
  <ul class="abs contact">
    <li><svg width="9" height="10" viewBox="0 0 9 10"><path d="M4.5 0.5a3 3 0 0 1 3 3c0 2.2-3 5.8-3 5.8s-3-3.6-3-5.8a3 3 0 0 1 3-3z" fill="none" stroke="#fff" stroke-width=".9"/><circle cx="4.5" cy="3.5" r="1" fill="#fff"/></svg><span>Lindenhofweg 12,<br>10965 Berlin, Germany</span></li>
    <li><svg width="8" height="8" viewBox="0 0 8 8"><path d="M1.5 .5l1.4 1.6-.8 1.1a4.5 4.5 0 0 0 2.7 2.7l1.1-.8 1.6 1.4-.9 1.1C3.9 7.4.6 4.1.4 1.4z" fill="#fff"/></svg><span>030 / 555 019 27</span></li>
    <li><svg width="9" height="7" viewBox="0 0 9 7"><rect x=".5" y=".5" width="8" height="6" fill="none" stroke="#fff" stroke-width=".9"/><path d="M.5 .5l4 3.2 4-3.2" fill="none" stroke="#fff" stroke-width=".9"/></svg><span>anfrage@quornel-energie.de</span></li>
    <li><svg width="8" height="8" viewBox="0 0 8 8"><circle cx="4" cy="4" r="3.5" fill="none" stroke="#fff" stroke-width=".8"/><ellipse cx="4" cy="4" rx="1.5" ry="3.5" fill="none" stroke="#fff" stroke-width=".7"/><path d="M.5 4h7" stroke="#fff" stroke-width=".7"/></svg><span>www.quornel-energie.de</span></li>
  </ul>
  <div class="abs partners-label">Unsere Partner</div>
  <div class="abs partners">
    <span>Ostnetz</span>
    <span>Helvion</span>
    <span style="font-size:11px;font-weight:700;line-height:11px;text-align:right">Stadtnetz<br>Spree</span>
  </div>

  <div class="abs brand-main"><span class="sq"></span>QUORNEL<span class="sub">ENERGIE</span></div>
  <div class="abs hero-photo" role="img" aria-label="Foto: dunkelblaues Holzhaus mit Solarmodulen auf dem Dach vor blauem Himmel"></div>
  <h1 class="abs hero-title">SAUBERE STROMERZEU­GUNG MITHILFE VON EINER PHOTOVOLTAIK-ANLAGE.</h1>
  <p class="abs hero-sub">Kontaktiere uns jetzt für ein unverbindliches erst Gespräch.</p>

  <!-- inner side -->
  <h2 class="abs heading self-title">Selbst zum Stromerzeuger werden mit der Photovoltaik-Anlage.</h2>
  <p class="abs copy self-copy">Du hast ein Eigenheim und/oder besitzt Immobilien mit genügend Platz auf dem Dach, dann ist eine Photovoltaik-Anlage eine gute Option.</p>
  <h3 class="abs heading reasons-title">Dafür gibt es mehrere gute Gründe:</h3>
  <ul class="abs reasons">
    <li><svg width="17" height="17" viewBox="0 0 17 17"><circle cx="8.5" cy="8.5" r="7.6" fill="none" stroke="var(--green)" stroke-width="1.4"/><path d="M5 8.7l2.4 2.3 4.6-4.8" fill="none" stroke="var(--green)" stroke-width="1.4"/></svg><span>Du wirst unabhängiger von den öffentlichen Stromanbietern</span></li>
    <li><svg width="17" height="17" viewBox="0 0 17 17"><circle cx="8.5" cy="8.5" r="7.6" fill="none" stroke="var(--green)" stroke-width="1.4"/><path d="M5 8.7l2.4 2.3 4.6-4.8" fill="none" stroke="var(--green)" stroke-width="1.4"/></svg><span>Du leistest einen Beitrag zur Energiewende und zum Klimaschutz</span></li>
    <li><svg width="17" height="17" viewBox="0 0 17 17"><circle cx="8.5" cy="8.5" r="7.6" fill="none" stroke="var(--green)" stroke-width="1.4"/><path d="M5 8.7l2.4 2.3 4.6-4.8" fill="none" stroke="var(--green)" stroke-width="1.4"/></svg><span>Photovoltaik ist eine saubere Form der Energieer­zeugung, da keine Schadstoffe ausgestoßen werden</span></li>
    <li><svg width="17" height="17" viewBox="0 0 17 17"><circle cx="8.5" cy="8.5" r="7.6" fill="none" stroke="var(--green)" stroke-width="1.4"/><path d="M5 8.7l2.4 2.3 4.6-4.8" fill="none" stroke="var(--green)" stroke-width="1.4"/></svg><span>Einspeisevergütung wird gezahlt, wenn der Strom in ein öffentliches Netz verkauft wird</span></li>
    <li><svg width="17" height="17" viewBox="0 0 17 17"><circle cx="8.5" cy="8.5" r="7.6" fill="none" stroke="var(--green)" stroke-width="1.4"/><path d="M5 8.7l2.4 2.3 4.6-4.8" fill="none" stroke="var(--green)" stroke-width="1.4"/></svg><span>Du sparst Stromkosten, wenn Du den Strom selbst nutzt</span></li>
    <li><svg width="17" height="17" viewBox="0 0 17 17"><circle cx="8.5" cy="8.5" r="7.6" fill="none" stroke="var(--green)" stroke-width="1.4"/><path d="M5 8.7l2.4 2.3 4.6-4.8" fill="none" stroke="var(--green)" stroke-width="1.4"/></svg><span>Eine PV Anlage kann mit Elektromobilität kombi­niert werden</span></li>
    <li><svg width="17" height="17" viewBox="0 0 17 17"><circle cx="8.5" cy="8.5" r="7.6" fill="none" stroke="var(--green)" stroke-width="1.4"/><path d="M5 8.7l2.4 2.3 4.6-4.8" fill="none" stroke="var(--green)" stroke-width="1.4"/></svg><span>PV-Anlagen kommen mit wenig Wartung aus Lebensdauer einer PV-Anlage liegt bei ca. 20 bis 25 Jahren</span></li>
    <li><svg width="17" height="17" viewBox="0 0 17 17"><circle cx="8.5" cy="8.5" r="7.6" fill="none" stroke="var(--green)" stroke-width="1.4"/><path d="M5 8.7l2.4 2.3 4.6-4.8" fill="none" stroke="var(--green)" stroke-width="1.4"/></svg><span>Förderung für die Errichtung von PV-Anlagen ist möglich</span></li>
  </ul>
  <div class="abs fill reasons-art" role="img" aria-label="Illustration: Haus mit Solardach, Glühbirne, Stecker, Batterie und Elektroauto in grüner Landschaft"></div>

  <div class="abs fill city-art" role="img" aria-label="Illustration: Stadt und Fabrik mit Solarfeldern, Straßenlaternen und Bäumen"></div>
  <div class="abs copy mid-copy">
    <p>Gerade angesichts der aktuell stark steigenden Stromkosten ist es sinnvoll, den Strom mit einer PV-Anlage selbst zu erzeugen und zu nutzen. Die Einspeisung wird pro Kilowattstunde durch den Örtliche Stromnetzbetreiber vergütet, diese Einspei­severgütung wird ab dem Inbetriebnahme Monat festgesetzt.<br>Die Einsparung pro Kilowattstunde Strom aus der PV-Anlage, den Du selbst<br>nutzt, ist deutlich höher als die zu erwartende Einspeisevergütung. Entscheidest Du Dich für eine vollumfängliche PV-Anlage mit Speicher, so kannst Du deinen Strombedarf selbst erzeugen, Speichern und den Strom auch dann nutzen, wenn die Sonne nicht scheint.</p>
    <p>Mit einem Batteriespeicher und einer PV-Anlage als Insellösung bist Du völlig unabhängig, da Du den Strom komplett selbst nutzt. Solche Insellösungen sind für Ferienhäuser geeignet, die keine Energiev­ersorgung durch einen örtlichen Energieversorger erhalten.</p>
  </div>

  <svg class="abs bg-curve" viewBox="0 0 538 260" aria-hidden="true"><path d="M0 260 C220 230 420 140 538 0 L538 260 Z" fill="#f4f4f4"/></svg>
  <h2 class="abs heading install-title">Die Installation von Photovoltaikan­lagen auf verschiedenen Flächen</h2>
  <p class="abs copy install-copy">Eine Photovoltaikanlage kann nicht nur auf dem Dach Deines Hauses installiert werden, sondern auch auf Garagen, Carports Industriedächern und Freiflächen. So lassen sich komplette Solarparks errichten. Die PV-Modul Dachmontage sollte so erfolgen, dass die Erträge an Strom möglichst hoch sind.<br>Optimal ist ein Dach mit Südausrichtung, doch geeignet sind auch Dächer mit Südwest-, Südost- und Ostwest Ausrichtung, allerdings fallen die Erträge dann geringer aus.</p>
  <ul class="abs areas">
    <li style="height:44px;padding-left:0"><span class="ico" role="img" aria-label="Symbol Carport"></span><span style="margin-left:0">Carport</span></li>
    <li style="height:44px;margin-top:4px"><span class="ico" role="img" aria-label="Symbol Garage"></span>Garage</li>
    <li style="height:44px;margin-top:9px"><span class="ico" role="img" aria-label="Symbol Industriefläche"></span>Industrieflächen</li>
    <li style="height:44px;margin-top:13px"><span class="ico" role="img" aria-label="Symbol Dach"></span><span style="margin-left:10px">Dächer</span></li>
  </ul>
  <div class="abs fill install-art" role="img" aria-label="Illustration: Monteure installieren Solarmodule auf einem Hausdach, Sonne und Lieferwagen"></div>

</main>
</body>
</html>
```